Educational Textbook Covern Design for mostly females

Create a textbook cover (will be white spiral) using the Brandguide.pdf attached. This will be a textbook given to mostly age 18-25 year old women so a modern trendy cute type design is wanted.
The book cover is 8.5" x 11" which will be printed in CMYK full bleed.
The name "BelvaLPN's Dental Hygiene Academy" must be on the cover somewhere and "BelvaLPN" has to be either the same height or larger height than the "Dental Hygiene Academy"

Please no real life photos such as images of dentists, etc. This should be all created art.

The year "2025" should be in the design as well.

IMPORTANT UPDATED 8/4/2024
These designs should not look too childish. This should be a professional textbook for dental professionals. All the current designs have too much cartoon art.

Target Market(s)

18-25 year old females

Industry/Entity Type

Dentistry

Font styles to use
Other font styles liked:
• See brand guide

Colors
A7469A
B969AE
D3A5CF
EDDBEB
F8F0F9
6B429C
8869AF
B7A5CE
E3DAEB
F3F0F8

Requirements
Should not have
• No photos, should be all art

```html
<!DOCTYPE html>
<html lang="en">
<head>
<meta charset="utf-8">
<title>BelvaLPN's Dental Hygiene Academy – 2025 Textbook Cover</title>
<link rel="stylesheet" href="https://fonts.googleapis.com/css2?family=Chewy&family=Fredoka:wght@700&display=swap">
<style>
  :root {
    --lilac: #9e7bb5;
    --plum: #472d7c;
    --sun: #e8cd35;
    --year-tint: rgba(237, 210, 46, 0.48);
    --shadow: rgba(58, 48, 62, 0.55);
  }
  html, body {
    margin: 0;
    padding: 0;
    overflow: hidden;
    background: var(--lilac);
  }
  .cover {
    position: relative;
    width: 927px;
    height: 1200px;
    overflow: hidden;
    background: var(--lilac);
  }
  .cover__backdrop {
    position: absolute;
    inset: 0;
    width: 927px;
    height: 1200px;
  }
  .wave { fill: var(--plum); }
  .year-row {
    font-family: "Fredoka", sans-serif;
    font-weight: 700;
    font-size: 440px;
    fill: var(--year-tint);
  }
  .mascot-shadow { fill: var(--shadow); }
  .title-band {
    position: absolute;
    left: 0;
    top: 161px;
    width: 927px;
    height: 295px;
    background: var(--sun);
    display: flex;
    flex-direction: column;
    align-items: center;
    justify-content: center;
    margin: 0;
    font-family: "Chewy", sans-serif;
    font-weight: 400;
    color: var(--plum);
    text-transform: uppercase;
    text-align: center;
    line-height: 1;
  }
  .title-band__name {
    display: block;
    font-size: 66px;
    letter-spacing: 1px;
  }
  .title-band__rest {
    display: block;
    font-size: 54px;
    margin-top: 14px;
    letter-spacing: 1px;
  }
  .mascot {
    position: absolute;
    left: 154px;
    top: 574px;
    width: 520px;
    height: 405px;
    border-radius: 48% 48% 40% 40%;
    background: radial-gradient(ellipse at 50% 45%, #f4f4f4 0%, #8a6fb5 45%, var(--plum) 75%);
  }
</style>
</head>
<body>
  <main class="cover">
    <svg class="cover__backdrop" viewBox="0 0 1688 2184" preserveAspectRatio="none" aria-hidden="true">
      <path class="wave" d="M648,0 H1688 V420 L820,700 C960,900 1010,1150 920,1380 C830,1600 600,1720 350,1830 C180,1920 60,2010 0,2110 V620 L800,320 C700,220 640,90 648,0 Z"/>
      <g class="year-rows" text-anchor="middle">
        <text class="year-row" x="845" y="405" textLength="900" lengthAdjust="spacingAndGlyphs">2025</text>
        <text class="year-row" x="845" y="825" textLength="900" lengthAdjust="spacingAndGlyphs">2025</text>
        <text class="year-row" x="845" y="1245" textLength="900" lengthAdjust="spacingAndGlyphs">2025</text>
        <text class="year-row" x="845" y="1665" textLength="900" lengthAdjust="spacingAndGlyphs">2025</text>
        <text class="year-row" x="845" y="2085" textLength="900" lengthAdjust="spacingAndGlyphs">2025</text>
      </g>
      <ellipse class="mascot-shadow" cx="770" cy="1785" rx="470" ry="70"/>
    </svg>

    <h1 class="title-band">
      <span class="title-band__name">BelvaLPN's Dental</span>
      <span class="title-band__rest">Hygiene Academy</span>
    </h1>

    <div class="mascot" role="img" aria-label="Illustration of a smiling tooth mascot wearing a graduation cap and round glasses, holding a rolled diploma"></div>
  </main>
</body>
</html>
```